Waymarchers Postcard Flyer

I run a group called 'The London Waymarchers Group', we explore London's history and culture through it's museums, art galleries, historical buildings, guided walks, theatre etc

I would need a design for a postcard sized flyer, full colour, double sided which will attract people to join the group if handed one.

Target Market(s)

People who like exploring museums, galleries, culture etc.

Industry/Entity Type

Group

Requirements
Must have
• The below needs to be included on the front:

www.waymarchers-club.org
The London Waymarchers Group
Meet like minded people!
Explore London's history and culture!
Join online

Also the panorama in the file attached.

The below needs to be included on the back:

www.waymarchers-club.org
We organise trips visiting: museums, art galleries, historical buildings, stately homes, theatre, guided walks, social/quiz nights, day trips out of London.

Also include some pictures of in the Word doc attached.

```html
<!DOCTYPE html>
<html lang="en">
<head>
<meta charset="utf-8">
<title>Waymarchers Postcard Flyer – Back</title>
<link rel="stylesheet" href="https://fonts.googleapis.com/css2?family=Lilita+One&family=Indie+Flower&display=swap">
<style>
  :root {
    --card-bg: #dff2b3;
    --brand-green: #79b52a;
    --ink: #141414;
    --frame: #ffffff;
    --shadow: rgba(0, 0, 0, 0.35);
    --ceiling-dark: #3b2716;
    --ceiling-gold: #a8844a;
    --portrait-wall: #c9c4a8;
    --portrait-olive: #6d7148;
    --portrait-coat: #2f5a3e;
    --lake-light: #7f9cbf;
    --lake-deep: #3f5a6e;
  }
  * { box-sizing: border-box; margin: 0; padding: 0; }
  html, body { width: 1200px; height: 917px; overflow: hidden; }
  body { background: var(--card-bg); }

  .flyer {
    position: relative;
    width: 1200px;
    height: 917px;
    background: var(--card-bg);
    overflow: hidden;
  }

  .site-address {
    position: absolute;
    top: 10px;
    left: 0;
    width: 100%;
    text-align: center;
    font-family: "Lilita One", sans-serif;
    font-size: 54px;
    font-weight: 400;
    letter-spacing: 0.5px;
    color: var(--brand-green);
  }

  .snapshot {
    position: absolute;
    background: var(--frame);
    padding: 12px;
    box-shadow: 3px 4px 8px var(--shadow);
  }
  .snapshot-fill { width: 100%; height: 100%; }

  .snapshot--ceiling {
    left: 93px; top: 125px; width: 245px; height: 305px;
    transform: rotate(-9deg);
  }
  .snapshot--ceiling .snapshot-fill {
    background: radial-gradient(ellipse at 50% 40%, var(--ceiling-gold), var(--ceiling-dark) 75%);
  }

  .snapshot--lake {
    left: 140px; top: 518px; width: 446px; height: 342px;
  }
  .snapshot--lake .snapshot-fill {
    background: linear-gradient(to bottom, var(--lake-light), var(--lake-deep));
  }

  .snapshot--portrait {
    left: 272px; top: 283px; width: 280px; height: 292px;
    padding: 14px 14px 40px;
    transform: rotate(5deg);
  }
  .snapshot--portrait .snapshot-fill {
    background: radial-gradient(ellipse at 50% 50%, var(--portrait-coat) 0%, var(--portrait-olive) 45%, var(--portrait-wall) 80%);
  }

  .trip-list {
    position: absolute;
    left: 686px;
    top: 172px;
    font-family: "Indie Flower", cursive;
    color: var(--ink);
  }
  .trip-list-heading {
    font-size: 51px;
    font-weight: 400;
    line-height: 1;
    margin-bottom: 30px;
  }
  .trip-list ul {
    list-style: none;
    padding-left: 56px;
  }
  .trip-list li {
    font-size: 41px;
    line-height: 70px;
  }
</style>
</head>
<body>
  <main class="flyer">
    <h1 class="site-address">www.waymarchers-club.org</h1>

    <figure class="snapshot snapshot--ceiling">
      <div class="snapshot-fill" role="img" aria-label="Photo of an ornate painted ceiling in a historic hall"></div>
    </figure>

    <figure class="snapshot snapshot--lake">
      <div class="snapshot-fill" role="img" aria-label="Photo of a park lake with trees and a palace in the distance"></div>
    </figure>

    <figure class="snapshot snapshot--portrait">
      <div class="snapshot-fill" role="img" aria-label="Photo of a framed portrait painting hanging in a gallery"></div>
    </figure>

    <section class="trip-list">
      <h2 class="trip-list-heading">We organise trips:</h2>
      <ul>
        <li>museums</li>
        <li>art galleries</li>
        <li>historical buildings</li>
        <li>stately homes</li>
        <li>theatres</li>
        <li>guided walks</li>
        <li>social/quiz nights</li>
        <li>daytrips out of London</li>
      </ul>
    </section>
  </main>
</body>
</html>
```